Webdesign für  Kranken- und Seniorenpflege
Webdesign für Kranken- und Seniorenpflege
Zielgruppe
Ambulante Kranken- und Seniorenpflege
Tagespflege in Limbach-Oberfrohna, Mittweida und Chemnitz
Palliativpflege
Aufgabenstellung
- Erstellung in Adobe Photoshop
- Orientieren Sie sich am Socialmedia-Auftritt des Kunden

```html
<!DOCTYPE html>
<html lang="de">
<head>
<meta charset="utf-8">
<title>Pflegehafen – Ambulante Kranken- und Seniorenpflege</title>
<link href="https://fonts.googleapis.com/css2?family=Open+Sans:wght@400;600;700&display=swap" rel="stylesheet">
<style>
:root{
  --berry:#99003f;
  --sun:#fbb314;
  --white:#ffffff;
  --mist:#ececec;
  --slate:#6d6d6d;
  --text-grey:#7a7a7a;
}
*{box-sizing:border-box;margin:0;padding:0}
html,body{width:1200px;height:2750px;overflow:hidden}
body{position:relative;background:var(--white);font-family:"Open Sans",sans-serif;color:var(--berry)}
.abs{position:absolute}
.site-header{left:0;top:0;width:1200px;height:112px}
.brand{left:62px;top:26px;display:flex;align-items:center;gap:12px;font-size:30px;font-weight:700;color:var(--berry)}
.brand-dot{width:56px;height:56px;border-radius:50%;background:var(--sun)}
.main-nav{right:113px;top:44px;display:flex;font-size:17px;font-weight:600}
.main-nav a{color:var(--berry);text-decoration:none;padding:0 28px;border-left:3px solid var(--sun);line-height:24px}
.main-nav a:first-child{border-left:none}
.main-nav a:last-child{padding-right:0}
.hotline{left:0;top:112px;width:1200px;height:62px;background:var(--berry);color:var(--white);font-size:24px;font-weight:600;text-align:center;line-height:62px}
.hero{left:0;top:174px;width:1200px;height:563px;background:linear-gradient(120deg,#c9b8a4,#a8c7d8 45%,#d7c9b2 75%,#9a9a88)}
.care-band{left:0;top:737px;width:1200px;height:331px;background:var(--sun)}
.care-title{left:0;top:762px;width:1200px;text-align:center;font-size:44px;font-weight:600;color:var(--white);text-shadow:0 2px 6px rgba(0,0,0,.25)}
.service-card{top:853px;width:303px;height:350px;background:var(--white);box-shadow:0 2px 8px rgba(0,0,0,.12);text-align:center}
.service-photo{position:absolute;left:50px;top:38px;width:203px;height:203px;border-radius:50%}
.service-label{position:absolute;left:0;right:0;top:265px;height:70px;display:flex;align-items:center;justify-content:center;font-size:22px;font-weight:700;line-height:30px}
.news{left:0;top:1273px;width:1200px;height:332px;background:var(--mist)}
.news-title{left:143px;top:1322px;font-size:34px;font-weight:400}
.news-text{left:143px;top:1396px;width:920px;font-size:22px;line-height:30px;color:var(--text-grey)}
.news-button{left:143px;top:1519px;width:150px;height:37px;background:var(--berry);color:var(--white);border-radius:5px;font-size:18px;font-weight:600;text-align:center;line-height:37px}
.slider-arrow{top:1410px}
.slider-dots{left:566px;top:1573px;display:flex;gap:8px}
.slider-dots span{width:10px;height:10px;border-radius:50%;border:1px solid #999}
.slider-dots span.active{background:#555;border-color:#555}
.jobs-photo{left:0;top:1655px;width:600px;height:420px;background:linear-gradient(110deg,#8aa3b8,#e7ece9 50%,#c5cbd0)}
.jobs-panel{left:600px;top:1655px;width:600px;height:420px;background:var(--berry)}
.panel-title{width:600px;text-align:center;font-size:34px;font-weight:600;color:var(--white)}
.job-button{left:673px;width:414px;height:104px;background:var(--white);border-radius:5px;display:flex;align-items:center;justify-content:center;text-align:center;font-size:22px;font-weight:700;line-height:30px;color:var(--berry)}
.places-panel{left:0;top:2131px;width:600px;height:421px;background:var(--sun)}
.places-photo{left:600px;top:2131px;width:600px;height:421px;background:linear-gradient(160deg,#8fc6ef,#d6ebf7 55%,#b9d7ec)}
.place-button{left:113px;width:414px;height:56px;background:var(--white);border-radius:5px;text-align:center;line-height:56px;font-size:22px;font-weight:700;color:var(--sun)}
.site-footer{left:0;top:2601px;width:1200px;height:149px;background:var(--slate)}
.social{top:2657px;width:36px;height:36px;border-radius:50%;background:var(--white)}
.footer-nav{right:113px;top:2662px;display:flex;font-size:17px;font-weight:600}
.footer-nav a{color:var(--white);text-decoration:none;padding:0 22px;border-left:3px solid var(--sun);line-height:24px}
.footer-nav a:first-child{border-left:none}
.footer-nav a:last-child{padding-right:0}
</style>
</head>
<body>
<header class="abs site-header">
  <div class="abs brand"><span class="brand-dot"></span>Pflegehafen</div>
  <nav class="abs main-nav">
    <a href="#">Pflegehafen</a><a href="#">Pflege</a><a href="#">Beratung</a><a href="#">Standorte</a><a href="#">Karriere</a>
  </nav>
</header>
<div class="abs hotline">Wir sind jederzeit kostenfrei für Sie da: Tel. 0800 5550199</div>
<div class="abs hero" role="img" aria-label="Foto: Pflegerin mit lachenden Senioren an einem Tisch auf der Terrasse"></div>

<section>
  <div class="abs care-band"></div>
  <h1 class="abs care-title">Ambulante Kranken- und Seniorenpflege</h1>
  <div class="abs service-card" style="left:112px">
    <div class="service-photo" role="img" aria-label="Foto: Pflegerin mit Seniorin im Rollstuhl" style="background:linear-gradient(135deg,#5f8fb8,#d9c3ad)"></div>
    <div class="service-label">Kranken- und<br>Seniorenpflege</div>
  </div>
  <div class="abs service-card" style="left:448px">
    <div class="service-photo" role="img" aria-label="Foto: Senior beim Schachspiel" style="background:linear-gradient(135deg,#e8e1d4,#7f95b5)"></div>
    <div class="service-label">Tagespflege</div>
  </div>
  <div class="abs service-card" style="left:784px">
    <div class="service-photo" role="img" aria-label="Foto: Seniorenpaar im Beratungsgespräch" style="background:linear-gradient(135deg,#c9c7c0,#8a7462)"></div>
    <div class="service-label">Pflegeberatung</div>
  </div>
</section>

<section>
  <div class="abs news"></div>
  <h2 class="abs news-title">Sommerfest in der Tagespflege „Lindenhof“</h2>
  <p class="abs news-text">Sommereinklang in der Tagespflege „Lindenhof“ in Chemnitz. Bei sommerlichen Temperaturen und strahlenden Sonnenschein verweilten die Tagesgäste auf unserer großzügigen Terrasse. Unsere Betreuungskraft Katrin sorgte für …</p>
  <div class="abs news-button">Weiterlesen</div>
  <svg class="abs slider-arrow" style="left:46px" width="32" height="58" viewBox="0 0 32 58"><path d="M30 2 L3 29 L30 56" fill="none" stroke="#555" stroke-width="2.5"/></svg>
  <svg class="abs slider-arrow" style="left:1122px" width="32" height="58" viewBox="0 0 32 58"><path d="M2 2 L29 29 L2 56" fill="none" stroke="#555" stroke-width="2.5"/></svg>
  <div class="abs slider-dots"><span></span><span class="active"></span><span></span><span></span></div>
</section>

<section>
  <div class="abs jobs-photo" role="img" aria-label="Foto: lächelnder Pfleger reicht einem Senior die Hand"></div>
  <div class="abs jobs-panel"></div>
  <h2 class="abs panel-title" style="left:600px;top:1690px">Aktuelle Stellenagebote</h2>
  <div class="abs job-button" style="top:1785px">Pflegeassistent/<br>Altenpflegehelfer (m/w)</div>
  <div class="abs job-button" style="top:1923px">Pflegefachkraft/<br>Altenpfleger (m/w)</div>
</section>

<section>
  <div class="abs places-panel"></div>
  <h2 class="abs panel-title" style="left:0;top:2166px">Unsere Standorte</h2>
  <div class="abs place-button" style="top:2260px">Chemnitz</div>
  <div class="abs place-button" style="top:2341px">Mittweida</div>
  <div class="abs place-button" style="top:2422px">Limbach-Oberfrohna</div>
  <div class="abs places-photo" role="img" aria-label="Foto: Hand hält eine rote Standortmarkierung vor blauem Himmel"></div>
</section>

<footer class="abs site-footer"></footer>
<div class="abs social" style="left:40px" aria-label="Social Media"></div>
<div class="abs social" style="left:87px" aria-label="Social Media"></div>
<div class="abs social" style="left:134px" aria-label="E-Mail">
  <svg width="36" height="36" viewBox="0 0 36 36"><rect x="9" y="12" width="18" height="13" fill="none" stroke="#6d6d6d" stroke-width="1.6"/><path d="M9 12 L18 19 L27 12" fill="none" stroke="#6d6d6d" stroke-width="1.6"/></svg>
</div>
<nav class="abs footer-nav"><a href="#">Kontakt</a><a href="#">Impressum</a><a href="#">Datenschutz</a></nav>
</body>
</html>
```